I am looking for help designing my new business cards. I would like rounded edges and a raised logo on the back of the card. I have 2 Logos. One with a boat in it and one without. I'd like the one on the back to be the one that includes the boat and just the name on the front. I have included multiple formats of my logo. Please let me know if you need anymore.

Target Market(s)

Potential buyers and other sales brokers

Industry/Entity Type

Sales - Yacht / Boat Sales

Contact Information for Business Card

Id liike the front to include just the business name portion of the logo along with my name (Corwin Dalby), phone number (555.318.6027), website address (www.dalbymarineco.example) and not my physical address but just "Harlow Bay, GA". The back should include my full logo that has the boat included. This portion I'd prefer raised amd take up the majority of the space there. Thanks!!

Colors
0054AA
0677BA
7BADD7
CADEEF
E8F1F8
0094D4
00A9DD
6FCCEA
C7EBF8
E9F6FB

Requirements
Must have
• Double sided
Nice to have
• My email address: Corwin@dalbymarineco.example The NMTG logo somewhere small on the front of the card
Should not have
• My full address, prefer only "Harlow Bay, GA"

```html
<!DOCTYPE html>
<html lang="en">
<head>
<meta charset="utf-8">
<title>Dalby Marine Co — Business Cards</title>
<link rel="stylesheet" href="https://fonts.googleapis.com/css2?family=Montserrat:wght@300;400;600;700;800&display=swap">
<style>
  :root {
    --backdrop: #808080;
    --navy: #1e2d5f;
    --sky: #1c86c6;
    --white: #ffffff;
    --shadow: rgba(0, 0, 0, 0.35);
  }
  html, body {
    margin: 0;
    padding: 0;
    width: 1200px;
    height: 855px;
    overflow: hidden;
    background: var(--backdrop);
    font-family: "Montserrat", sans-serif;
  }
  .stage {
    position: relative;
    width: 1200px;
    height: 855px;
  }
  .card {
    position: absolute;
    background: var(--navy);
    border-radius: 18px;
    overflow: hidden;
    box-shadow: 6px 8px 14px var(--shadow);
    color: var(--white);
  }
  .card__footer-band {
    position: absolute;
    left: 0;
    right: 0;
    bottom: 0;
    background: var(--sky);
  }

  .brand-name {
    position: absolute;
    left: 0;
    right: 0;
    font-weight: 800;
    color: var(--white);
    letter-spacing: 0.5px;
    line-height: 1;
    white-space: nowrap;
    display: flex;
    justify-content: center;
    align-items: center;
    gap: 7px;
  }
  .brand-name__dot {
    width: 10px;
    height: 10px;
    border-radius: 50%;
    background: var(--sky);
    flex: none;
  }

  /* Front */
  .card--front {
    left: 129px;
    top: 140px;
    width: 326px;
    height: 573px;
  }
  .card--front .card__footer-band { height: 13px; }
  .card--front .brand-name {
    top: 129px;
    font-size: 22px;
  }
  .name-band {
    position: absolute;
    left: 0;
    right: 0;
    top: 259px;
    height: 57px;
    background: var(--sky);
    display: flex;
    align-items: center;
    justify-content: center;
  }
  .name-band__name {
    font-weight: 600;
    font-size: 25px;
    letter-spacing: 0.3px;
    text-transform: uppercase;
  }
  .divider {
    position: absolute;
    left: 74px;
    right: 74px;
    display: flex;
    align-items: center;
    gap: 4px;
  }
  .divider__line {
    flex: 1;
    height: 1px;
    background: var(--sky);
  }
  .divider__icons {
    display: flex;
    gap: 3px;
    padding: 0 6px;
  }
  .icon {
    width: 20px;
    height: 20px;
    border-radius: 50%;
    background: var(--sky);
    display: flex;
    align-items: center;
    justify-content: center;
  }
  .icon svg { width: 11px; height: 11px; }
  .divider--contact { top: 362px; }
  .divider--location { top: 474px; }
  .contact-list {
    position: absolute;
    left: 0;
    right: 0;
    top: 392px;
    margin: 0;
    padding: 0;
    list-style: none;
    text-align: center;
    font-weight: 400;
    font-size: 13px;
    line-height: 20.5px;
    letter-spacing: 0.2px;
  }
  .location {
    position: absolute;
    left: 0;
    right: 0;
    top: 505px;
    text-align: center;
    font-size: 13px;
    letter-spacing: 0.6px;
    text-transform: uppercase;
  }

  /* Back */
  .card--back {
    left: 505px;
    top: 384px;
    width: 579px;
    height: 329px;
  }
  .card--back .card__footer-band { height: 17px; }
  .vessel-art {
    position: absolute;
    left: 165px;
    top: 72px;
    width: 251px;
    height: 116px;
    border-radius: 8px;
    background: linear-gradient(180deg, rgba(255,255,255,0.18) 0%, rgba(28,134,198,0.55) 100%);
  }
  .card--back .brand-name {
    top: 211px;
    font-size: 26px;
    gap: 8px;
  }
  .card--back .brand-name__dot {
    width: 12px;
    height: 12px;
  }
</style>
</head>
<body>
<main class="stage">

  <section class="card card--front" aria-label="Business card front">
    <div class="brand-name"><span class="brand-name__dot"></span>DALBY MARINE CO</div>

    <div class="name-band">
      <span class="name-band__name">Corwin Dalby</span>
    </div>

    <div class="divider divider--contact">
      <span class="divider__line"></span>
      <span class="divider__icons">
        <span class="icon" aria-label="Phone">
          <svg viewBox="0 0 24 24"><path fill="#fff" d="M6.6 10.8a15.1 15.1 0 0 0 6.6 6.6l2.2-2.2c.3-.3.7-.4 1-.2 1.1.4 2.3.6 3.6.6.6 0 1 .4 1 1V20c0 .6-.4 1-1 1A17 17 0 0 1 3 4c0-.6.4-1 1-1h3.5c.6 0 1 .4 1 1 0 1.3.2 2.5.6 3.6.1.3 0 .7-.2 1z"/></svg>
        </span>
        <span class="icon" aria-label="Email">
          <svg viewBox="0 0 24 24"><rect x="2" y="5" width="20" height="14" rx="1.5" fill="#fff"/><path d="M3 6l9 7 9-7" stroke="#1c86c6" stroke-width="2" fill="none"/></svg>
        </span>
        <span class="icon" aria-label="Website">
          <svg viewBox="0 0 24 24"><circle cx="12" cy="12" r="9" fill="none" stroke="#fff" stroke-width="2"/><ellipse cx="12" cy="12" rx="4" ry="9" fill="none" stroke="#fff" stroke-width="2"/><path d="M3 12h18" stroke="#fff" stroke-width="2"/></svg>
        </span>
      </span>
      <span class="divider__line"></span>
    </div>

    <ul class="contact-list">
      <li>555.318.6027</li>
      <li>Corwin@dalbymarineco.example</li>
      <li>www.dalbymarineco.example</li>
    </ul>

    <div class="divider divider--location">
      <span class="divider__line"></span>
      <span class="divider__icons">
        <span class="icon" aria-label="Location">
          <svg viewBox="0 0 24 24"><path fill="#fff" d="M12 2a7 7 0 0 0-7 7c0 5.2 7 13 7 13s7-7.8 7-13a7 7 0 0 0-7-7zm0 9.5A2.5 2.5 0 1 1 12 6.5a2.5 2.5 0 0 1 0 5z"/></svg>
        </span>
      </span>
      <span class="divider__line"></span>
    </div>

    <div class="location">Harlow Bay, GA</div>

    <div class="card__footer-band"></div>
  </section>

  <section class="card card--back" aria-label="Business card back">
    <div class="vessel-art" role="img" aria-label="Illustration of a center-console sport boat cutting through a blue wave"></div>
    <div class="brand-name"><span class="brand-name__dot"></span>DALBY MARINE CO</div>
    <div class="card__footer-band"></div>
  </section>

</main>
</body>
</html>
```